Real Estate Business Cards

Looking for a clean, sharp and professional look for our Real Estate investment Fund that invests in Multi Family Apartment buildings.

Target Market(s)

Real Estate Fund

Industry/Entity Type

Real Estate

Contact Information for Business Card

Company Description: Real Estate Investment Fund
Company Name: RKW Holdings
Name: Marcus Olvane
Cell: (917) 482-0657
Email: marcus@rkwholdings-example.com
Website: www.rkwholdings-example.com
Address: 418, 9th Street, Brooklyn NY 11218

Colors

Designer to choose colors to be used in the design.

Requirements
Nice to have
• Colors to match logo

```html
<!DOCTYPE html>
<html lang="en">
<head>
<meta charset="utf-8">
<title>RKW Holdings – Business Cards</title>
<link href="https://fonts.googleapis.com/css2?family=Cinzel:wght@400&family=Lato:wght@300;400&display=swap" rel="stylesheet">
<style>
  :root {
    --page-bg: #d9d6d1;
    --card-bg: #efefef;
    --card-tone: #e7e7e7;
    --ink: #4a4a4a;
    --ink-soft: #5a5a5a;
    --brand-blue: #1f6fae;
    --band: #4b4b4b;
  }
  * { box-sizing: border-box; margin: 0; padding: 0; }
  html, body { width: 1200px; height: 900px; overflow: hidden; }
  body {
    background: var(--page-bg);
    font-family: "Lato", "Helvetica Neue", Arial, sans-serif;
    color: var(--ink);
    position: relative;
  }
  .card {
    position: absolute;
    left: 250px;
    width: 700px;
    height: 400px;
    background: var(--card-bg);
    overflow: hidden;
    box-shadow: 0 6px 18px rgba(0,0,0,0.18);
  }
  .card--back { top: 40px; }
  .card--front { top: 470px; }
  .card__texture {
    position: absolute; inset: 0;
    background: linear-gradient(135deg, var(--card-bg), var(--card-tone));
  }
  .brand {
    position: relative;
    display: flex;
    align-items: center;
    font-family: "Cinzel", "Times New Roman", serif;
    color: var(--ink);
  }
  .brand__mark {
    width: 14px; height: 14px;
    background: var(--brand-blue);
  }

  /* back */
  .brand-block {
    position: absolute; left: 0; right: 0; top: 40px;
    display: flex; flex-direction: column; align-items: center;
  }
  .brand-block__mark { width: 70px; height: 70px; background: var(--brand-blue); margin-bottom: 26px; }
  .brand-block .brand__name { font-family: "Cinzel", "Times New Roman", serif; font-size: 44px; letter-spacing: 2px; color: var(--ink); }
  .brand__tagline {
    margin-top: 8px;
    font-size: 17px;
    letter-spacing: 2.5px;
    color: var(--ink-soft);
  }

  /* front */
  .card--front .brand {
    position: absolute; left: 40px; top: 34px; gap: 14px;
  }
  .card--front .brand__mark { width: 40px; height: 40px; }
  .card--front .brand__name { font-size: 22px; letter-spacing: 1px; }
  .person {
    position: absolute; left: 36px; top: 160px;
    width: 385px;
  }
  .person__name {
    font-size: 37px; font-weight: 400; line-height: 1; letter-spacing: 0.5px; color: var(--ink);
    white-space: nowrap;
  }
  .person__title {
    margin-top: 8px; margin-left: 38px;
    font-size: 18px; font-weight: 400; letter-spacing: 1.5px; color: var(--ink-soft);
  }
  .divider {
    position: absolute; left: 438px; top: 176px;
    width: 3px; height: 160px; background: var(--ink);
  }
  .contact {
    position: absolute; left: 454px; top: 180px; right: 12px;
    list-style: none;
    font-size: 12.5px; color: var(--ink); line-height: 1.3;
  }
  .contact__item { display: flex; align-items: flex-start; gap: 8px; margin-bottom: 14px; white-space: nowrap; }
  .contact__icon { width: 16px; height: 16px; flex: none; fill: var(--ink); }
  .footer-band {
    position: absolute; left: 112px; right: 112px; bottom: 0;
    height: 30px; background: var(--band);
    border-radius: 22px 22px 0 0;
  }
</style>
</head>
<body>

  <section class="card card--back" aria-label="Business card back">
    <div class="card__texture" role="img" aria-label="Fine light grey geometric background pattern"></div>
    <div class="brand-block">
      <span class="brand-block__mark"></span>
      <span class="brand__name">RKW Holdings</span>
      <p class="brand__tagline">REAL ESTATE INVESTMENT FUND</p>
    </div>
  </section>

  <section class="card card--front" aria-label="Business card front">
    <div class="card__texture" role="img" aria-label="Fine light grey geometric background pattern"></div>

    <div class="brand">
      <span class="brand__mark"></span>
      <span class="brand__name">RKW Holdings</span>
    </div>

    <div class="person">
      <h1 class="person__name">MARCUS OLVANE</h1>
      <p class="person__title">GENERAL MANAGER</p>
    </div>

    <div class="divider"></div>

    <ul class="contact">
      <li class="contact__item">
        <svg class="contact__icon" viewBox="0 0 24 24"><path d="M6.6 10.8a15.1 15.1 0 0 0 6.6 6.6l2.2-2.2a1 1 0 0 1 1-.25 11.4 11.4 0 0 0 3.6.57 1 1 0 0 1 1 1V20a1 1 0 0 1-1 1A17 17 0 0 1 3 4a1 1 0 0 1 1-1h3.5a1 1 0 0 1 1 1c0 1.25.2 2.45.57 3.57a1 1 0 0 1-.25 1z"/></svg>
        <span>(917) 482-0657</span>
      </li>
      <li class="contact__item">
        <svg class="contact__icon" viewBox="0 0 24 24"><path d="M12 2a7 7 0 0 0-7 7c0 5.25 7 13 7 13s7-7.75 7-13a7 7 0 0 0-7-7zm0 9.5A2.5 2.5 0 1 1 12 6.5a2.5 2.5 0 0 1 0 5z"/></svg>
        <span>418, 9th Street,<br>Brooklyn NY 11218</span>
      </li>
      <li class="contact__item">
        <svg class="contact__icon" viewBox="0 0 24 24"><path d="M2 5h20v14H2zm2 2v.4l8 5.6 8-5.6V7zm0 2.8V17h16V9.8l-8 5.6z"/></svg>
        <span>marcus@rkwholdings-example.com</span>
      </li>
      <li class="contact__item">
        <svg class="contact__icon" viewBox="0 0 24 24"><path d="M12 2a10 10 0 1 0 0 20 10 10 0 0 0 0-20zm6.9 6h-3a15.7 15.7 0 0 0-1.4-3.6A8 8 0 0 1 18.9 8zM12 4c.8 1.2 1.5 2.5 1.9 4h-3.8c.4-1.5 1.1-2.8 1.9-4zM4.3 14a8 8 0 0 1 0-4h3.4a16.5 16.5 0 0 0 0 4zm.8 2h3a15.7 15.7 0 0 0 1.4 3.6A8 8 0 0 1 5.1 16zm3-8h-3a8 8 0 0 1 4.4-3.6A15.7 15.7 0 0 0 8.1 8zM12 20c-.8-1.2-1.5-2.5-1.9-4h3.8c-.4 1.5-1.1 2.8-1.9 4zm2.3-6H9.7a14.7 14.7 0 0 1 0-4h4.6a14.7 14.7 0 0 1 0 4zm.2 5.6a15.7 15.7 0 0 0 1.4-3.6h3a8 8 0 0 1-4.4 3.6zm1.8-5.6a16.5 16.5 0 0 0 0-4h3.4a8 8 0 0 1 0 4z"/></svg>
        <span>www.rkwholdings-example.com</span>
      </li>
    </ul>

    <div class="footer-band"></div>
  </section>

</body>
</html>
```